Environmental Consultancey needs Web Design

A consultancey firm based in Papua New Guinea specialising servicing a client market primarily in Melanesia, the wider Pacific Region and South East Asia. The firm provides services to community development and resource extraction activites that incorporate sustainable livelihoods for local customary land owners with environmentally responsibile practices and a focus on maintaining biodiversity and ecosystem services. We aim to encompass Culture, Custom and Science in our approach. Our website preferentially will convey a relaxed Pacific Island feel in its colours and design rather than a sterile corporate feel. See attached logo that will need to be visible on page or which may provide basis for ideas for the page.

Target Market(s)

Our target market is primarily the oil, gas and mining industry, secondarily international donor and aid programs followed by government projects and not for profit programs. Services include:
1. Biodiversity and Conservation - Fauna and Flora survey, assessment, management, monitoring & research, protected areas & endangered & threatend species.
2. Social & Community - impact, stakeholder engagement, census and survey, land and community affairs, capacity building empowerment.
3. Environmental Management - sustainable use, enterprise development & management, biodiversity offsets.

Industry/Entity Type

Community

Requirements
Must have
• Multiple pages, Logo somewhere on home page. Space for a couple of photos that as yet ive not decieded upon.
Nice to have
• Perhaps incorporate shapes, texture and colours that convey a feel of the attached photo of a blue bird of paradise. The blue fine overlapping and interlocking feather patterns are appealing perhaps as a background and the other colours used in boarders ? Abstract is fine as would be symbolic images or tribal ambience. The company is all about blending humanity in all its forms with the environment.

```html
<!DOCTYPE html>
<html lang="en">
<head>
<meta charset="utf-8">
<title>Kinaki Environs — Culture, Custom &amp; Science</title>
<link href="https://fonts.googleapis.com/css2?family=Source+Sans+3:wght@400;600;700&display=swap" rel="stylesheet">
<style>
:root{
  --page:#ffffff;
  --ink:#222222;
  --body:#3a3a3a;
  --link:#17788a;
  --bar-top:#4fd2ec;
  --bar-mid:#35bcd9;
  --bar-low:#1f94b0;
  --frame:#d8d8d8;
  --dot-blue:#7fb6c6;
  --dot-grey:#8a8a8a;
}
*{box-sizing:border-box;margin:0;padding:0}
html,body{width:1200px;height:1031px;overflow:hidden;background:var(--page)}
body{position:relative;font-family:"Source Sans 3",Arial,sans-serif;color:var(--body)}
.abs{position:absolute}

.nav-bar{left:141px;top:42px;width:918px;height:31px;border-radius:15px;
  background:linear-gradient(to bottom,var(--bar-top),var(--bar-mid) 55%,var(--bar-low))}
.nav{position:absolute;left:398px;top:0;height:31px;display:flex;list-style:none}
.nav li{height:31px;line-height:31px;color:#fff;font-size:13.5px;text-align:center;
  border-left:1px solid rgba(255,255,255,.45);box-shadow:-1px 0 0 rgba(0,80,100,.25)}
.brand{left:155px;top:0;width:120px;height:118px;border-radius:50%;background:#fff;
  box-shadow:0 1px 3px rgba(0,0,0,.15);display:flex;align-items:center;justify-content:center;
  text-align:center;font-size:15px;font-weight:600;color:#2a6f80;line-height:1.15}

.hero-photo{left:141px;top:87px;width:613px;height:282px;
  background:linear-gradient(160deg,#6f7f86 0%,#8f7b5c 30%,#a48c6a 55%,#5d6a3c 80%,#3f4a2a 100%)}
.hero-title{left:786px;top:104px;font-size:27px;font-weight:700;line-height:34px;color:var(--ink);letter-spacing:.6px}
.hero-text{left:789px;top:211px;width:250px;font-size:12px;line-height:17.6px}
.dots{left:885px;top:351px;display:flex;gap:7px}
.dots span{width:8px;height:8px;border-radius:50%;background:var(--dot-blue)}
.dots span:last-child{background:var(--dot-grey)}

h2{position:absolute;font-weight:400;color:var(--ink)}
.welcome-title{left:141px;top:385px;font-size:27px}
.welcome-text{left:141px;top:424px;width:512px;font-size:12px;line-height:19.6px}
.more{font-size:12px;color:var(--link);letter-spacing:.3px}
.news-title{left:717px;top:389px;font-size:23px}
.news-date{left:719px;top:428px;font-size:13px;font-weight:700;color:var(--ink);letter-spacing:.5px}
.news-text{left:717px;top:450px;width:345px;font-size:12px;line-height:16px}

.projects-title{left:141px;top:585px;font-size:23px}
.story-title{left:685px;top:585px;font-size:23px}
.thumb{width:137px;height:131px;background:#fff;border:1px solid var(--frame);
  box-shadow:0 1px 3px rgba(0,0,0,.2);padding:3px}
.thumb div{width:100%;height:100%}
.story-photo{left:690px;top:628px;width:369px;height:131px;background:#fff;border:1px solid var(--frame);
  box-shadow:0 1px 3px rgba(0,0,0,.2);padding:3px}
.story-photo div{width:100%;height:100%;background:linear-gradient(90deg,#5a3c2a,#8a7550 45%,#6e7a45 75%,#4e5a33)}
.story-lead{left:698px;top:783px;width:340px;font-size:13.3px;line-height:19.6px}
.story-text{left:698px;top:863px;width:345px;font-size:11px;line-height:19.5px}

.footer{left:141px;top:963px;width:918px;height:68px;
  background:linear-gradient(to bottom,var(--bar-top),var(--bar-mid) 45%,var(--bar-low));
  color:#fff;text-align:center;font-size:10.5px;line-height:16px;padding-top:21px;letter-spacing:.2px}
</style>
</head>
<body>
<header>
  <div class="abs nav-bar">
    <ul class="nav">
      <li style="width:79px">Home</li>
      <li style="width:98px">About us</li>
      <li style="width:125px">Our Activities</li>
      <li style="width:95px">Services</li>
      <li style="width:108px">Contact us</li>
    </ul>
  </div>
  <div class="abs brand">Kinaki<br>Environs</div>
</header>

<section>
  <div class="abs hero-photo" role="img" aria-label="Photo of thatched-roof village huts among tropical plants"></div>
  <h1 class="abs hero-title">Encompassing<br>Culture, Custom<br>&amp; Science</h1>
  <p class="abs hero-text">Lorem Ipsum is simply dummy text of the printing and typesetting industry. Lorem Ipsum has been the industry's standard dummy text ever since the 1500s, when an unknown printer took a galley of type and scrambled it to make a type specimen book.</p>
  <div class="abs dots"><span></span><span></span><span></span></div>
</section>

<section>
  <h2 class="welcome-title">Welcome</h2>
  <p class="abs welcome-text">Lorem Ipsum is simply dummy text of the printing and typesetting industry. Lorem Ipsum has been the industry's standard dummy text ever since the 1500s, when an unknown printer took a galley of type and scrambled it to make a type specimen book. Ipsum has been the industry's standard dummy text ever since the 1500s, when an unknown printer took a galley of type and scrambled it to make a type specimen book. Ipsum has been the industry's</p>
  <a class="abs more" style="left:605px;top:546px">view all</a>

  <h2 class="news-title">Latest News</h2>
  <div class="abs news-date">05 - 12 - 12</div>
  <p class="abs news-text">Lorem Ipsum is simply dummy text of the printing and type-setting industry. Lorem Ipsum has been the industry's standard dummy text ever since the 1500s, when an unknown printer took a galley of type and scrambled it to make a type specimen book.</p>
  <a class="abs more" style="left:719px;top:546px">view all news</a>
</section>

<section>
  <h2 class="projects-title">Our Projects</h2>
  <div class="abs thumb" style="left:156px;top:628px"><div role="img" aria-label="Photo of a yellow snail on a branch" style="background:linear-gradient(135deg,#4f8a2c,#b9a640 50%,#5a4a30)"></div></div>
  <div class="abs thumb" style="left:325px;top:628px"><div role="img" aria-label="Photo of a stilt house in the forest" style="background:linear-gradient(180deg,#8fa56a,#6a5a3c 55%,#5f9a34)"></div></div>
  <div class="abs thumb" style="left:495px;top:628px"><div role="img" aria-label="Photo of red and orange tropical fruit" style="background:linear-gradient(135deg,#5c6e2c,#c96a4c 50%,#7a3a2c)"></div></div>
  <div class="abs thumb" style="left:156px;top:802px"><div role="img" aria-label="Photo of orange flowers" style="background:linear-gradient(135deg,#e88a4a,#d9662e 50%,#3f6a2a)"></div></div>
  <div class="abs thumb" style="left:325px;top:802px"><div role="img" aria-label="Photo of a netted stinkhorn fungus" style="background:linear-gradient(180deg,#4a3c2a,#cfc9bd 60%,#3a3024)"></div></div>
  <div class="abs thumb" style="left:495px;top:802px"><div role="img" aria-label="Photo of a group of village community members" style="background:linear-gradient(180deg,#6a6a5a,#7a4a3a 50%,#b87a8a)"></div></div>

  <h2 class="story-title">Our Story</h2>
  <div class="abs story-photo"><div role="img" aria-label="Photo of a man with a large turtle in a garden"></div></div>
  <p class="abs story-lead">Lorem Ipsum is simply dummy text of the printing and typesetting industry. Lorem Ipsum has been the indus-try's standard dummy text ever since the 1500s,</p>
  <p class="abs story-text">when an unknown printer took a galley of type and scrambled it to make a type specimen book.</p>
  <a class="abs more" style="left:1013px;top:920px">view all</a>
</section>

<footer class="abs footer">
  © 2012 Kinaki Environs<br>
  Terms of Service - Privacy Policy - Program Policies
</footer>
</body>
</html>
```